Carrowfield Banner- Real Estate Luxury Sale Banner

I need a large banner for an outside of a construction building.

It should say
THE CARROWFIELD
100 Carrowfield Street, East Boston – A Boutique Collection of Four Luxury Residences

Experience refined living with elegant design, high-end finishes, and expansive private decks in every residence. Thoughtfully crafted for both comfort and sophistication, each home features a modern fireplace and exceptional attention to detail.

Residence One – 2 Bed | 3 Bath | Private Yard + Large Deck
Residence Two – 2 Bed | 2 Bath | Spacious Deck
Residence Three – 2 Bed | 2 Bath | Expansive Deck
Residence Four – 2 Bed | 2 Bath | Panoramic Roof Deck with Stunning Boston Views
Now Accepting Reservations – Limited Availability

Schedule Your Private Tour Today

Marisa Thornquist, Larkspur Realty | 617-555-0192 | marisa@larkspurhomesmail.com
Construction by Pine Arch Builders

Target Market(s)

ages 30-50

Industry/Entity Type

real estate

Font styles to use
Serif

Requirements
Must have
• classic look
Nice to have
• colors of navy and gold

```html
<!DOCTYPE html>
<html lang="en">
<head>
<meta charset="utf-8">
<title>The Carrowfield – Luxury Residences Banner</title>
<link rel="stylesheet" href="https://fonts.googleapis.com/css2?family=Cormorant+Garamond:wght@500;600&family=Libre+Caslon+Text:ital,wght@0,400;0,700;1,400;1,700&display=swap">
<style>
  :root {
    --navy: #263558;
    --navy-deep: #1b2538;
    --navy-ink: #1f2d52;
    --gold: #e3b15c;
    --gold-soft: #d8ad6b;
    --white: #ffffff;
    --paper: #ffffff;
    --grey: #6c7080;
  }
  * { margin: 0; padding: 0; box-sizing: border-box; }
  html, body { width: 1200px; height: 480px; overflow: hidden; background: var(--navy-deep); }
  .banner {
    position: relative; width: 1200px; height: 480px; overflow: hidden;
    background: var(--navy);
    font-family: "Libre Caslon Text", Georgia, serif;
    color: var(--white);
  }
  .brand-band { position: absolute; left: 0; top: 354px; width: 1200px; height: 70px; background: var(--navy-deep); }
  .footer-bar { position: absolute; left: 0; top: 424px; width: 1200px; height: 45px; background: var(--paper); }
  .footer-edge { position: absolute; left: 0; top: 469px; width: 1200px; height: 11px; background: var(--navy-deep); }

  .glow { position: absolute; left: 508px; top: 240px; }
  .building-photo {
    position: absolute; left: 600px; top: 37px; width: 183px; height: 387px;
    background: linear-gradient(180deg, #45474c 0%, #3a3c41 60%, #8c6446 62%, #a87a52 85%, #6d7487 100%);
  }

  /* left column */
  .title {
    position: absolute; left: 40px; top: 34px; width: 490px; text-align: center;
    font-family: "Cormorant Garamond", "Times New Roman", serif; font-weight: 500;
    font-size: 62px; line-height: 1; font-variant: small-caps; letter-spacing: 0.5px;
  }
  .title-rule {
    position: absolute; left: 123px; top: 109px; width: 322px; height: 2px;
    background: linear-gradient(90deg, rgba(227,177,92,0), var(--gold) 20%, var(--gold) 80%, rgba(227,177,92,0));
  }
  .address {
    position: absolute; left: 40px; top: 127px; width: 490px; text-align: center;
    font-size: 17px; letter-spacing: 0.3px;
  }
  .address svg { vertical-align: -2px; margin-right: 8px; }
  .headline {
    position: absolute; left: 30px; top: 164px; width: 510px; text-align: center;
    font-style: italic; font-weight: 700; font-size: 34px; line-height: 39px;
  }
  .intro {
    position: absolute; left: 40px; top: 250px; width: 490px; text-align: center;
    font-size: 13.2px; line-height: 16.3px;
  }

  /* residences */
  .residences { position: absolute; left: 874px; top: 62px; width: 300px; text-align: center; }
  .residence { height: 63px; }
  .residence-name { color: var(--gold); font-size: 19px; line-height: 24px; }
  .residence-specs { font-size: 13.5px; line-height: 18px; }
  .sep { color: var(--gold-soft); margin: 0 4px; }

  /* brand band */
  .agency { position: absolute; left: 34px; top: 368px; display: flex; align-items: center; gap: 12px; }
  .agency-mark { width: 42px; height: 42px; border: 2px solid var(--gold); border-radius: 50%; }
  .agency-name { color: var(--gold); font-size: 20px; letter-spacing: 1px; text-transform: uppercase; }

  .availability { position: absolute; left: 874px; top: 362px; width: 300px; text-align: center; }
  .availability-lead { font-size: 17.5px; letter-spacing: 0.6px; line-height: 24px; }
  .availability-pill {
    display: inline-block; margin-top: 3px; padding: 0 16px; height: 25px; line-height: 23px;
    border: 1.5px solid var(--gold); border-radius: 13px; color: var(--gold); font-size: 17px;
  }

  /* footer */
  .tour-tab { position: absolute; left: 0; top: 424px; }
  .tour-text {
    position: absolute; left: 33px; top: 424px; height: 45px; line-height: 45px;
    font-size: 16.5px; color: var(--white);
  }
  .contact {
    position: absolute; left: 378px; top: 424px; height: 45px; line-height: 45px;
    font-size: 15.5px; color: var(--navy-ink); white-space: nowrap;
  }
  .builder {
    position: absolute; left: 1000px; top: 424px; height: 45px; line-height: 45px;
    white-space: nowrap; color: var(--navy-ink);
  }
  .builder-by { color: var(--grey); font-size: 15px; margin-right: 6px; }
  .builder-name { font-weight: 700; font-size: 13px; text-transform: uppercase; letter-spacing: 0.3px; }
</style>
</head>
<body>
<div class="banner">
  <div class="brand-band"></div>

  <svg class="glow" width="368" height="184" viewBox="0 0 368 184" aria-hidden="true">
    <defs>
      <linearGradient id="glowFill" x1="0" y1="0" x2="0" y2="1">
        <stop offset="0" stop-color="#263558"/>
        <stop offset="1" stop-color="#e8b560"/>
      </linearGradient>
    </defs>
    <path d="M0 184 A184 184 0 0 1 368 184 Z" fill="url(#glowFill)"/>
  </svg>

  <div class="building-photo" role="img" aria-label="Photograph of the four-storey Carrowfield building facade with dark vertical siding above, warm wood cladding at street level and a car parked in front"></div>

  <h1 class="title">The Carrowfield</h1>
  <div class="title-rule"></div>
  <p class="address">
    <svg width="12" height="16" viewBox="0 0 12 16" aria-hidden="true"><path d="M6 0C2.7 0 0 2.6 0 5.9 0 10 6 16 6 16s6-6 6-10.1C12 2.6 9.3 0 6 0zm0 8.2A2.3 2.3 0 1 1 6 3.6a2.3 2.3 0 0 1 0 4.6z" fill="#e3b15c"/></svg>100 Carrowfield Street, East Boston
  </p>
  <h2 class="headline">A Boutique Collection of Four<br>Luxury Residences</h2>
  <p class="intro">Experience refined living with elegant design, high–end finishes, and expansive private decks in every residence. Thoughtfully crafted for both comfort and sophistication, each home features a modern fireplace and exceptional attention to detail.</p>

  <div class="residences">
    <div class="residence">
      <div class="residence-name">Residence 1</div>
      <div class="residence-specs">2 Bed<span class="sep">|</span>3 Bath<span class="sep">|</span>Private Yard <span class="sep">+</span> Large Deck</div>
    </div>
    <div class="residence">
      <div class="residence-name">Residence 2</div>
      <div class="residence-specs">2 Bed<span class="sep">|</span>2 Bath<span class="sep">|</span>Spacious Deck</div>
    </div>
    <div class="residence">
      <div class="residence-name">Residence 3</div>
      <div class="residence-specs">2 Bed<span class="sep">|</span>2 Bath<span class="sep">|</span>Expansive Deck</div>
    </div>
    <div class="residence">
      <div class="residence-name">Residence 4</div>
      <div class="residence-specs">2 Bed<span class="sep">|</span>2 Bath<span class="sep">|</span>Panoramic Roof Deck<br>with Stunning Boston Views</div>
    </div>
  </div>

  <div class="agency">
    <div class="agency-mark"></div>
    <div class="agency-name">Larkspur Realty</div>
  </div>

  <div class="availability">
    <div class="availability-lead">Now Accepting Reservations</div>
    <div class="availability-pill">Limited Availability</div>
  </div>

  <div class="footer-bar"></div>
  <div class="footer-edge"></div>
  <svg class="tour-tab" width="380" height="45" viewBox="0 0 380 45" aria-hidden="true">
    <path d="M0 0 H372 C358 0 352 10 348 22 C344 35 338 45 320 45 H0 Z" fill="#d8ad6b"/>
  </svg>
  <div class="tour-text">Schedule Your Private Tour Today!</div>
  <div class="contact">Marisa Thornquist<span class="sep">|</span>(617) 555–0192<span class="sep">|</span>marisa@larkspurhomesmail.com</div>
  <div class="builder"><span class="builder-by">by</span><span class="builder-name">Pine Arch Builders</span></div>
</div>
</body>
</html>
```